Poster for Tradesmen Website

We had a soft launch of our website. The site brings together tradesmen jobseekers and customers to one virtual location. The website serves Australian market. To clearly understand what we mean please visit www.workmeld.com.au. For our future promotional campaign we intend to use poster which we intend to distribute in trade exhibits and in recruitment offices.
Color and Poster Design Content: - Very light blue is the predominant color of the website. The design is not limited on this color. They are free to explore other color if they think that will effectively convey the message of the poster. Presently our website uses images showing tradesmen in action as well as the customers. Designers can use these images or use other image in their design which will best suit their design
Size: - We are looking at poster printed A3 size, but the design should not limit their target size on A3 (it should be versatile, insure that the file format for your design support large-format printing without being pixilated) since we also want it printed in vinyl as stand-alone banner (example: 1200 x 1700 mm approx) that will be used in trade exhibits.
Message of the Poster:
For our first marketing campaign we want to join a trade expo which will be held on the last week of May 2012. For this expo we need a poster and a stand-alone banner to be displayed on our booth. The poster should convey the following message:
a) that a new website has been launched
b) that the website brings together tradesmen, customers and jobseekers to one virtual location
c) that for tradesmen the website is a venue to advertise their business
d) that for customers, it will make the task of finding the right tradies much easier
e) that for jobseekers the site is one way of finding a job by just posting their resume and potential employers can view the summary of their qualification and send notification if they are interested on a particular jobseeker.
Images:
We don't have any other high resolution images Except for the images that we used on our website. We got those images online. Besides, we are not sure what particular image will be appropriate for the poster. As the designer and the creative artist as well, you are free to use whatever images that you think is appropriate for the your design. We think any images (not necessarily tradesmen images) can be used as long as it can strongly convey our message. Again, as the creative artist it is up to you to decide what image is/are appropriate. The only thing we can tell you guys is that we can tell a good/excellent design when we see one.
Logo:
We don't have a logo yet for our website. For the purpose of this poster you can use the font used on website name:
workmeld.com.au
tradie {font-family:Arial, Helvetica, sans-serif; color:#407FC0;}
meld.com.au {font-family:Arial, Helvetica, sans-serif; color:#00007F;}
Target Market(s)
Age group: 18 - 65, Gender: male-female, Education: any
Industry/Entity Type
Marketing
Look and feel
Each slider illustrates characteristics of the customer's brand and the style your logo design should communicate.

```html
<!DOCTYPE html>
<html lang="en">
<head>
<meta charset="utf-8">
<title>WORKMELD.COM.AU – New Website Poster</title>
<link rel="stylesheet" href="https://fonts.googleapis.com/css2?family=Didact+Gothic&family=Roboto:wght@300&display=swap">
<style>
  :root {
    --navy: #375f85;
    --sky: #a9c7e2;
    --pale: #cddff0;
    --accent-red: #c0272d;
    --ink: #111111;
    --paper: #ffffff;
  }
  html, body {
    margin: 0;
    padding: 0;
    overflow: hidden;
    background: var(--paper);
  }
  .poster {
    position: relative;
    width: 848px;
    height: 1200px;
    overflow: hidden;
    background: var(--paper);
    font-family: "Didact Gothic", "Century Gothic", sans-serif;
    color: var(--ink);
  }
  .brand-name {
    position: absolute;
    left: 118px;
    width: 608px;
    margin: 0;
    font-family: "Roboto", Arial, sans-serif;
    font-weight: 300;
    font-size: 62px;
    line-height: 1;
    letter-spacing: 1px;
    color: var(--navy);
    text-align: center;
    white-space: nowrap;
  }
  .brand-name--top { top: 92px; }
  .brand-name--bottom { top: 1094px; }
  .headline {
    position: absolute;
    left: 118px;
    top: 155px;
    width: 608px;
    margin: 0;
    font-family: "Roboto", Arial, sans-serif;
    font-weight: 300;
    font-size: 40px;
    line-height: 1;
    color: var(--ink);
    display: flex;
    justify-content: space-between;
  }
  .rule-red {
    position: absolute;
    height: 2px;
    background: var(--accent-red);
  }
  .rule-red--header { left: 118px; top: 201px; width: 608px; }
  .intro {
    position: absolute;
    left: 120px;
    top: 257px;
    width: 600px;
    margin: 0;
    font-size: 18px;
    line-height: 26px;
    text-align: center;
  }
  .highlight { color: var(--accent-red); }
  .handshake {
    position: absolute;
    left: 118px;
    top: 372px;
    width: 610px;
    height: 336px;
    background: linear-gradient(90deg, var(--pale) 0%, var(--pale) 45%, var(--navy) 70%, var(--navy) 100%);
  }
  .audience {
    position: absolute;
    top: 752px;
    margin: 0;
    font-size: 18px;
    line-height: 27px;
  }
  .audience strong { font-weight: 400; display: block; }
  .audience--employers {
    left: 118px;
    padding-left: 5px;
    border-left: 2px solid var(--accent-red);
  }
  .audience--tradesmen {
    right: 122px;
    padding-right: 3px;
    border-right: 2px solid var(--accent-red);
    text-align: right;
  }
  .tagline {
    position: absolute;
    left: 253px;
    top: 918px;
    width: 334px;
    margin: 0;
    font-size: 20px;
    line-height: 24px;
    text-align: center;
    padding-bottom: 3px;
    border-bottom: 2px solid var(--accent-red);
  }
  .rule-dark {
    position: absolute;
    left: 116px;
    top: 1051px;
    width: 607px;
    height: 3px;
    background: var(--ink);
  }
  .signup {
    position: absolute;
    left: 120px;
    top: 1065px;
    width: 600px;
    margin: 0;
    font-size: 18px;
    text-align: center;
  }
</style>
</head>
<body>
  <main class="poster">
    <h1 class="brand-name brand-name--top">WORKMELD.COM.AU</h1>
    <h2 class="headline"><span>N</span><span>E</span><span>W</span><span>&nbsp;</span><span>W</span><span>E</span><span>B</span><span>S</span><span>I</span><span>T</span><span>E</span></h2>
    <div class="rule-red rule-red--header"></div>

    <p class="intro">Our fresh platform allows for correspondance<br>between <span class="highlight">tradesmen</span> and potential <span class="highlight">employers</span><br>in one virtual location.</p>

    <div class="handshake" role="img" aria-label="Flat illustration of a light blue hand and a dark blue hand meeting in a handshake"></div>

    <p class="audience audience--employers"><strong>EMPLOYERS</strong>advertise your business<br>and job postings</p>
    <p class="audience audience--tradesmen"><strong>TRADESMEN</strong>publish your resume<br>and qualifications</p>

    <p class="tagline">MAKE THE RIGHT CONNECTION</p>

    <div class="rule-dark"></div>
    <p class="signup">for more information and to sign up please visit</p>
    <p class="brand-name brand-name--bottom">WORKMELD.COM.AU</p>
  </main>
</body>
</html>
```